TalvenInsight card back

Our company already has a logo and we have business cards. (I have included a picture of my business card front that i plan to use.) I want to promote a new division of Talven, called "TalvenInsight" and would like the back side of my card designed to promote this division using the same color scheme and concept as front. So I'm looking for a design for the TalvenInsight (back) side of my card. This back side does need any contact info - including that it doesn't need my name, phone, email etc. I have included the tag line that I would like to have included on that TalvenInsight side of the card. But i'd like the design to reflect "wisdom" but using a similar theme as in our sun logo. One concept i have for this side of the card has the sun is entirely out of the box and lighting up a spacious blue background to the card. Then there's a "TalvenInsight" as well as the tag line. I welcome concepts along these lines or others that you may have. Thanks!

Target Market(s)

High-end energy, or technology firms. Business leaders within the firm.

Industry/Entity Type

Professional Service

Contact Information for Business Card

The card will be double sided, but i only the need the single TalvenInsight side designed. It has to coordinate with the front side (I've included a picture of it) in color, etc.

Logo Text

TalvenInsight

Font styles to use
Other font styles liked:
• font from existing card front

Requirements
Must have
• The tie in with the Talven sun from our logo. A sense of spaciousness and/or clarity that comes from enlightened wisdom. A professional feel but a feel good feel too. The division label "TalvenInsight" and in a similar font as the existing business card. The tag line.
Should not have
• The back, TalvenINsight, side should not have contact info and should not repeat any of the front side info, given that it will be printed on the back side of card.

```html
<!DOCTYPE html>
<html lang="en">
<head>
<meta charset="utf-8">
<title>TalvenInsight card back</title>
<link rel="stylesheet" href="https://fonts.googleapis.com/css2?family=Open+Sans:wght@400;600&display=swap">
<style>
  :root {
    --canvas: #ecebe8;
    --card-white: #ffffff;
    --navy: #0f2f66;
    --white: #ffffff;
    --shadow: rgba(20, 30, 50, 0.22);
  }
  html, body {
    margin: 0;
    padding: 0;
    width: 1200px;
    height: 1000px;
    overflow: hidden;
    background: var(--canvas);
  }
  .stage {
    width: 1200px;
    height: 1000px;
    display: flex;
    align-items: center;
    justify-content: center;
  }
  .card {
    width: 1050px;
    height: 600px;
    background: var(--card-white);
    box-shadow: 0 14px 40px var(--shadow);
    display: flex;
    flex-direction: column;
    overflow: hidden;
    font-family: "Open Sans", Arial, sans-serif;
  }
  .card__top {
    height: 132px;
    padding: 0 56px;
    display: flex;
    align-items: center;
  }
  .card__main {
    flex: 1;
    background: var(--navy);
    position: relative;
    display: flex;
    flex-direction: column;
    align-items: center;
    justify-content: center;
    gap: 22px;
    padding-bottom: 30px;
  }
  .division-name {
    font-weight: 600;
    line-height: 1.1;
    margin: 0;
  }
  .division-name--small {
    font-size: 30px;
    color: var(--navy);
  }
  .division-name--large {
    font-size: 56px;
    color: var(--white);
  }
  .tagline {
    margin: 0;
    font-size: 17px;
    font-weight: 400;
    color: var(--white);
    text-align: center;
  }
  .web {
    position: absolute;
    right: 52px;
    bottom: 30px;
    display: flex;
    align-items: center;
    gap: 14px;
    font-size: 17px;
    color: var(--white);
  }
  .web__icon { width: 20px; height: 20px; }
</style>
</head>
<body>
<main class="stage">
  <article class="card">
    <header class="card__top">
      <p class="division-name division-name--small">TalvenInsight</p>
    </header>
    <section class="card__main">
      <h1 class="division-name division-name--large">TalvenInsight</h1>
      <p class="tagline">Offering Vision, Creativity, And Resilience To Individuals And Organization</p>
      <div class="web">
        <svg class="web__icon" viewBox="0 0 20 20" fill="none" stroke="#ffffff" stroke-width="1.4" aria-hidden="true">
          <circle cx="10" cy="10" r="8.5"/>
          <ellipse cx="10" cy="10" rx="3.8" ry="8.5"/>
          <line x1="1.5" y1="10" x2="18.5" y2="10"/>
          <path d="M3 5.5h14M3 14.5h14"/>
        </svg>
        <span>www.talven.com</span>
      </div>
    </section>
  </article>
</main>
</body>
</html>
```